Property Management Company Business Cards

Need business cards for a property management company located in Michigan. We manage houses for clients all over the world. Young and modern company, looking for eye catching design. Please work with the attached logo.

Industry/Entity Type

Property Management

Requirements
Must have
• Need lines for address, telephone number, fax number, web site.

Also lines for name, and job title

```html
<!DOCTYPE html>
<html lang="en">
<head>
<meta charset="utf-8">
<title>Northwind Estate Management – Business Cards</title>
<link rel="stylesheet" href="https://fonts.googleapis.com/css2?family=Open+Sans:wght@300;400;700&display=swap">
<style>
  :root {
    --sky: #4fd4f8;
    --charcoal: #2a2f33;
    --paper: #ffffff;
    --edge-front: #9fe6fa;
    --edge-back: #8d9094;
    --page: #ffffff;
  }
  * { box-sizing: border-box; margin: 0; padding: 0; }
  html, body {
    width: 999px;
    height: 1200px;
    overflow: hidden;
    background: var(--page);
    font-family: "Open Sans", sans-serif;
  }
  .canvas { position: relative; width: 999px; height: 1200px; }

  .card {
    position: absolute;
    background: var(--paper);
    border-radius: 20px;
    overflow: hidden;
  }
  .card-front {
    left: 127px; top: 0; width: 866px; height: 518px;
    border: 2px solid var(--edge-front);
    border-top: none;
    border-radius: 0 0 20px 20px;
  }
  .card-back {
    left: 132px; top: 675px; width: 864px; height: 523px;
    border: 2px solid var(--edge-back);
  }
  .card-art { position: absolute; inset: 0; width: 100%; height: 100%; }
  .sky-fill { fill: var(--sky); }
  .charcoal-fill { fill: var(--charcoal); }

  /* front: holder details */
  .holder-name {
    position: absolute; right: 63px; top: 52px;
    font-size: 33px; font-weight: 400; color: var(--sky);
    letter-spacing: 0.5px;
  }
  .holder-role {
    position: absolute; right: 63px; top: 106px;
    font-size: 21px; font-weight: 400; color: var(--sky);
  }
  .contact-row {
    position: absolute; left: 466px; right: 63px;
    display: flex; align-items: center;
    font-size: 25px; font-weight: 300; color: var(--sky);
  }
  .contact-row.phone { top: 182px; }
  .contact-row.fax { top: 233px; }
  .contact-row.address { top: 284px; }
  .contact-label { width: 38px; }
  .contact-bar { width: 2px; height: 26px; background: var(--sky); }
  .contact-value { margin-left: auto; font-size: 25px; }

  /* company name blocks */
  .company {
    position: absolute; display: flex; align-items: center;
  }
  .company-dot { border-radius: 50%; flex: none; }
  .company-name {
    font-weight: 700; text-transform: uppercase; line-height: 1.05;
  }
  .company-front { left: 36px; top: 432px; gap: 12px; }
  .company-front .company-dot { width: 44px; height: 44px; background: var(--paper); }
  .company-front .company-name { color: var(--paper); font-size: 20px; }

  .company-back { left: 180px; top: 56px; gap: 18px; }
  .company-back .company-dot { width: 76px; height: 76px; background: var(--sky); }
  .company-back .company-name { color: var(--charcoal); font-size: 36px; }

  .email {
    position: absolute; left: 0; right: 0; top: 462px;
    text-align: center;
    font-size: 27px; font-weight: 400; color: var(--sky);
    letter-spacing: 1.5px;
  }
</style>
</head>
<body>
<main class="canvas">

  <section class="card card-front" aria-label="Business card front">
    <svg class="card-art" viewBox="0 0 526 315" preserveAspectRatio="none" aria-hidden="true">
      <path class="sky-fill" d="M20,0 C80,120 220,225 526,228 L526,248 C260,245 120,130 72,0 Z"/>
      <path class="charcoal-fill" d="M0,118 C120,210 300,265 526,254 L526,315 L0,315 Z"/>
    </svg>

    <h1 class="holder-name">YOUR NAME HERE</h1>
    <p class="holder-role">Position</p>

    <p class="contact-row phone"><span class="contact-label">P</span><span class="contact-bar"></span><span class="contact-value">+0012 3456 7891</span></p>
    <p class="contact-row fax"><span class="contact-label">F</span><span class="contact-bar"></span><span class="contact-value">+0012 3456 7891</span></p>
    <p class="contact-row address"><span class="contact-label">A</span><span class="contact-bar"></span><span class="contact-value">YOUR ADRESS HERE</span></p>

    <div class="company company-front">
      <span class="company-dot"></span>
      <p class="company-name">Northwind Estate<br>Management</p>
    </div>
  </section>

  <section class="card card-back" aria-label="Business card back">
    <svg class="card-art" viewBox="0 0 525 318" preserveAspectRatio="none" aria-hidden="true">
      <path class="sky-fill" d="M488,0 L525,0 L525,58 C400,160 210,238 0,262 L0,250 C210,222 390,128 488,0 Z"/>
      <path class="charcoal-fill" d="M0,270 C210,256 400,210 525,186 L525,318 L0,318 Z"/>
    </svg>

    <div class="company company-back">
      <span class="company-dot"></span>
      <p class="company-name">Northwind Estate<br>Management</p>
    </div>

    <p class="email">wwwwwww@wwwwww.www.com</p>
  </section>

</main>
</body>
</html>
```